Marlowe Fen Gin (bottle label)

Marlowe Fen Gin is a hand crafted spirit distilled by Tidewell Distillery. The distillery is farm based. This is our first offering. The label is to be applied to a glass bottle.

We chose the name because we felt lucky to chance upon a great recipe. So we came up with Marlowe Fen Gin. The phrase "Sometimes you get lucky" needs to be included. We'd like to see imagery of a lucky symbol such as a 4 leaf clover or shooting star. Elegant contrast come to mind. Reference to the distillery, bottle size (375ml) and Alc./vol. 40% is also needed. The distillery logo could be included. Or all is included in printed content.
Logo included for reference.
The label is rectangular.

Target Market(s)

Adults who enjoy fine spirits

Industry/Entity Type

Spirits distillation

Font styles to use
Serif
Script

Requirements
Must have
• classy, eye catching presentation
Nice to have
• Stylized 4 leaf clover or shooting star
Should not have
• Nothing hokey

```html
<!DOCTYPE html>
<html lang="en">
<head>
<meta charset="utf-8">
<title>Marlowe Fen Gin – Label</title>
<link href="https://fonts.googleapis.com/css2?family=Cinzel:wght@400;500&family=Roboto+Condensed:wght@300;400&display=swap" rel="stylesheet">
<style>
  :root {
    --page: #ffffff;
    --teal-deep: #2a948d;
    --teal-mid: #7fb5b1;
    --mist: #dfe3e3;
    --pearl: #efefef;
    --ink: #2f2f2f;
    --white: #ffffff;
    --emblem: rgba(255, 255, 255, 0.75);
  }
  html, body {
    margin: 0;
    padding: 0;
    width: 776px;
    height: 1200px;
    overflow: hidden;
    background: var(--page);
  }
  .label {
    position: relative;
    width: 776px;
    height: 1200px;
  }
  .label-disc {
    position: absolute;
    left: 0;
    top: 0;
    width: 776px;
    height: 1200px;
  }
  .brand-name {
    position: absolute;
    left: 0;
    width: 776px;
    top: 508px;
    text-align: center;
    font-family: "Cinzel", serif;
    font-weight: 400;
    font-size: 76px;
    line-height: 1;
    letter-spacing: -1px;
    color: var(--ink);
    margin: 0;
  }
  .subline {
    position: absolute;
    left: 150px;
    top: 604px;
    display: flex;
    align-items: center;
  }
  .spirit {
    font-family: "Cinzel", serif;
    font-size: 46px;
    line-height: 1;
    color: var(--white);
    letter-spacing: -1px;
  }
  .divider {
    width: 2px;
    height: 54px;
    background: var(--white);
    margin: 0 18px 0 14px;
  }
  .tagline {
    font-family: "Cinzel", serif;
    font-size: 19px;
    line-height: 1.05;
    letter-spacing: 3px;
    color: var(--ink);
    text-transform: uppercase;
  }
  .abv, .volume {
    position: absolute;
    font-family: "Roboto Condensed", sans-serif;
    font-weight: 300;
    font-size: 26px;
    line-height: 1;
  }
  .abv { left: 150px; top: 766px; color: var(--white); }
  .volume { left: 530px; top: 780px; color: var(--ink); }
</style>
</head>
<body>
  <main class="label">
    <svg class="label-disc" viewBox="0 0 776 1200" xmlns="http://www.w3.org/2000/svg">
      <defs>
        <linearGradient id="disc-fade" x1="0.15" y1="0.95" x2="0.8" y2="0.2">
          <stop offset="0" stop-color="var(--teal-deep)"/>
          <stop offset="0.35" stop-color="var(--teal-mid)"/>
          <stop offset="0.65" stop-color="var(--mist)"/>
          <stop offset="1" stop-color="var(--pearl)"/>
        </linearGradient>
        <radialGradient id="emblem-glow" cx="0.5" cy="0.5" r="0.5">
          <stop offset="0" stop-color="var(--emblem)"/>
          <stop offset="1" stop-color="rgba(255,255,255,0)"/>
        </radialGradient>
      </defs>
      <circle class="disc" cx="388" cy="600" r="340" fill="url(#disc-fade)"/>
      <rect class="shooting-star" x="282" y="274" width="235" height="230" rx="40"
            fill="url(#emblem-glow)" role="img" aria-label="Stylised white shooting star with a curved trail"/>
      <rect class="clover" x="267" y="730" width="253" height="180" rx="60"
            fill="url(#emblem-glow)" role="img" aria-label="Stylised white four leaf clover"/>
    </svg>

    <h1 class="brand-name">MARLOWE FEN</h1>

    <div class="subline">
      <span class="spirit">GIN</span>
      <span class="divider"></span>
      <span class="tagline">Sometimes<br>You get lucky</span>
    </div>

    <div class="abv">Alc./vol. 40%</div>
    <div class="volume">375ml</div>
  </main>
</body>
</html>
```